Brisket Glazing

Brisket Glazing company specializing in commercial fit outs, pool fencing, frameless showers and glass splash backs, im after a very young/modern logo, it doesnt have to be revelent to glazing and a classy "boss like" design for the card. thank you in advanced
Updates

im thinking carbon fiber back ground or something along that line with bright orange wording or something maybe, open to suggestions 

Industry/Entity Type

Fencing

Contact Information for Business Card

company name, name, phone and products

```html
<!DOCTYPE html>
<html lang="en">
<head>
<meta charset="utf-8">
<title>Brisket Glazing — Business Card</title>
<link href="https://fonts.googleapis.com/css2?family=Exo+2:wght@500&family=Roboto:wght@300;400;700&display=swap" rel="stylesheet">
<style>
  :root {
    --stage: #262827;
    --card-core: #2e2e2e;
    --card-edge: #0d0d0d;
    --orange: #f26c1f;
    --white: #f2f2f2;
    --soft: #d9d9d9;
    --rule: rgba(242,108,31,0.55);
    --divider: rgba(255,255,255,0.18);
  }
  * { margin: 0; padding: 0; box-sizing: border-box; }
  html, body { width: 1200px; height: 900px; overflow: hidden; background: var(--stage); }
  .stage { position: relative; width: 1200px; height: 900px; }
  .card {
    position: absolute; top: 293px; width: 517px; height: 313px;
    background:
      radial-gradient(ellipse at 50% 45%, var(--card-core) 0%, #1b1b1b 55%, var(--card-edge) 100%);
    box-shadow: 0 2px 10px rgba(0,0,0,0.35);
    overflow: hidden;
    font-family: "Roboto", Arial, sans-serif;
    color: var(--white);
  }
  .card--front { left: 71px; }
  .card--back { left: 612px; }

  .brand {
    position: absolute; left: 32px; top: 34px;
    display: flex; align-items: center; gap: 10px;
  }
  .brand__square { width: 30px; height: 30px; background: var(--orange); }
  .brand__name { font-weight: 700; font-size: 30px; color: var(--orange); letter-spacing: 0.5px; }

  .person { position: absolute; left: 28px; top: 160px; right: 0; }
  .person__name { font-weight: 700; font-size: 24px; color: var(--orange); line-height: 1; letter-spacing: 0.3px; }
  .person__role { font-size: 14px; font-weight: 400; color: var(--white); margin-top: 3px; }
  .person__rule {
    position: absolute; top: 13px; left: 180px; right: 0; height: 1px; background: var(--rule);
  }
  .person__rule--lead {
    position: absolute; top: 193px; left: 0; width: 22px; height: 1px; background: var(--rule);
  }

  .contact { position: absolute; left: 28px; top: 244px; font-size: 16px; font-weight: 300; line-height: 19.5px; }
  .contact__key { color: var(--orange); display: inline-block; width: 26px; }
  .address { position: absolute; right: 32px; top: 264px; text-align: right; font-size: 16px; font-weight: 300; line-height: 19.5px; }

  .back-brand {
    position: absolute; left: 40px; top: 120px; width: 190px;
    display: flex; flex-direction: column; align-items: center; gap: 12px;
  }
  .back-brand__square { width: 46px; height: 46px; background: var(--orange); }
  .back-brand__name { font-weight: 700; font-size: 24px; color: var(--orange); }
  .back-divider {
    position: absolute; left: 243px; top: 60px; width: 1px; height: 200px;
    background: linear-gradient(to bottom, transparent, var(--divider), transparent);
  }
  .services {
    position: absolute; left: 262px; top: 100px; list-style: none;
    font-family: "Exo 2", "Roboto", sans-serif; font-weight: 500; font-size: 18px; line-height: 28px;
  }
  .services li::before {
    content: ""; display: inline-block; width: 7px; height: 7px; border-radius: 50%;
    background: var(--orange); margin-right: 7px; vertical-align: middle; position: relative; top: -2px;
  }
</style>
</head>
<body>
<main class="stage">
  <section class="card card--front">
    <div class="brand">
      <span class="brand__square"></span>
      <span class="brand__name">Brisket Glazing</span>
    </div>
    <span class="person__rule--lead"></span>
    <div class="person">
      <p class="person__name">DALE CORWIN</p>
      <p class="person__role">Managing Director</p>
      <span class="person__rule"></span>
    </div>
    <div class="contact">
      <p><span class="contact__key">T :</span>+63 900 555 0142</p>
      <p><span class="contact__key">E :</span>dale@brisketglazing.com</p>
      <p><span class="contact__key">W:</span>www.brisketglazing.com</p>
    </div>
    <div class="address">
      <p>dummy dummy, dummy</p>
      <p>dummy City, dummy</p>
    </div>
  </section>

  <section class="card card--back">
    <div class="back-brand">
      <span class="back-brand__square"></span>
      <span class="back-brand__name">Brisket Glazing</span>
    </div>
    <span class="back-divider"></span>
    <ul class="services">
      <li>Commercial fit outs</li>
      <li>Pool fencing</li>
      <li>Frameless showers</li>
      <li>Glass splash backs</li>
    </ul>
  </section>
</main>
</body>
</html>
```